business card design - photography

I am a fine art photographer. I would like to approach galleries to exhibit my work and need a business card.

The card should convey creativity and simplicity.
I would like a double sided card.

Some options:
1. An all white card with raised or embossed text or design to create a tactile finish.
2. a white and dark grey design would also work well.
3. Would be great to use my name as part of the design but not essential.
4. My name and title on the front, other details on the back of card.

The final design should be simple, minimal, elegant and innovative.
Being minimal, it will be more about texture, text size and placement.

examples of designs I would prefer provided here:
http://layoutmuse.net/ideas/40-plain-and-graceful-calling-card-layouts

I'm also open to other designs that may be unusual and unique.

Love this:
http://www.snapvault.com/pics/morningverses/583017264
Updates

I have uploaded a psd file after playing around in photoshop with various fonts.  I like the font (which I downloaded from typeshelf.net called Arual) but the design probably needs some refining.  I hope this helps.  If you'd like me to change the format of the file, please let me know.

Marta

Target Market(s)

Art Gallery owners/administrators and customers.

Industry/Entity Type

Business

Requirements
Must have
• A unique look.

Matte, silky finish or heavy textured stock. Double-sided card.

Front:
my name
photography by

Back:
phone no
email
web address
Nice to have
• Letterpress
embrossed
Clean fonts
Should not have
• Do not use illustrations of cameras or lenses.
No frames around the card edge.

```html
<!DOCTYPE html>
<html lang="en">
<head>
<meta charset="utf-8">
<title>Marta Vennick Photography – Business Card</title>
<link rel="stylesheet" href="https://fonts.googleapis.com/css2?family=Questrial&family=Arimo:wght@400&display=swap">
<style>
  :root {
    --backdrop: #4b3527;
    --card: #f2f2f1;
    --card-edge: #dcdcda;
    --ink: #3b3b3c;
    --ink-soft: #555657;
    --band: #5a5c5f;
    --band-text: #2f3032;
    --note: #e0141b;
  }
  * { margin: 0; padding: 0; box-sizing: border-box; }
  html, body { width: 1200px; height: 900px; overflow: hidden; }
  body {
    position: relative;
    background: var(--backdrop);
    font-family: "Questrial", "Century Gothic", sans-serif;
    color: var(--ink);
  }
  .card {
    position: absolute;
    background: var(--card);
    border: 1px solid var(--card-edge);
    overflow: hidden;
    box-shadow: 0 2px 6px rgba(0,0,0,0.35);
  }
  .card--front { left: 90px; top: 174px; width: 431px; height: 270px; }
  .card--detail { left: 566px; top: 56px; width: 499px; height: 276px; }
  .card--back-one { left: 90px; top: 461px; width: 431px; height: 266px; }
  .card--back-two { left: 630px; top: 461px; width: 431px; height: 270px; }

  .wordmark { position: absolute; white-space: nowrap; }
  .wordmark__name {
    display: block;
    letter-spacing: -0.04em;
    line-height: 1;
    color: var(--ink);
    text-shadow: 0 1px 0 rgba(255,255,255,0.9), 0 -1px 0 rgba(0,0,0,0.18);
  }
  .wordmark__title {
    display: block;
    font-family: "Arimo", Arial, sans-serif;
    font-style: italic;
    line-height: 1;
    color: var(--ink);
  }
  .card--front .wordmark { left: 79px; top: 120px; }
  .card--front .wordmark__name { font-size: 44px; }
  .card--front .wordmark__title { font-size: 10px; letter-spacing: 1.05em; margin-top: 1px; padding-left: 6px; }

  .card--detail .wordmark { left: 49px; top: 66px; }
  .card--detail .wordmark__name { font-size: 104px; text-shadow: 0 2px 1px rgba(255,255,255,0.95), 0 -2px 2px rgba(0,0,0,0.22); }
  .card--detail .wordmark__title { font-size: 25px; letter-spacing: 1.1em; margin-top: 4px; padding-left: 14px; }

  .contact {
    position: absolute;
    font-family: "Arimo", Arial, sans-serif;
    font-size: 10px;
    line-height: 17px;
    color: var(--ink-soft);
    list-style: none;
  }
  .card--back-one .contact { left: 24px; top: 104px; }
  .card--back-two .contact { left: 0; right: 0; top: 104px; text-align: center; }

  .band {
    position: absolute;
    background: var(--band);
    display: flex;
    align-items: center;
    font-size: 17px;
    letter-spacing: -0.03em;
    color: var(--band-text);
    white-space: nowrap;
  }
  .card--back-one .band { left: 0; right: 0; bottom: 0; height: 30px; justify-content: flex-end; padding-right: 16px; }
  .card--back-two .band { left: 0; bottom: 0; width: 186px; height: 36px; justify-content: center; }

  .note {
    position: absolute;
    font-family: "Arimo", Arial, sans-serif;
    font-size: 24px;
    color: var(--note);
    white-space: nowrap;
  }
  .note--front { left: 169px; top: 120px; }
  .note--detail { left: 668px; top: 380px; width: 360px; text-align: center; line-height: 26px; }
  .note--back-one { left: 169px; top: 746px; }
  .note--back-two { left: 722px; top: 746px; }
  .note-arrow { position: absolute; left: 816px; top: 340px; }
</style>
</head>
<body>
  <p class="note note--front">front design</p>

  <section class="card card--front" aria-label="Card front">
    <h1 class="wordmark">
      <span class="wordmark__name">MARTA VENNICK</span>
      <span class="wordmark__title">PHOTOGRAPHY</span>
    </h1>
  </section>

  <section class="card card--detail" aria-label="Card front, close-up of letterpress finish">
    <div class="wordmark">
      <span class="wordmark__name">MARTA VENNICK</span>
      <span class="wordmark__title">PHOTOGRAPHY</span>
    </div>
  </section>

  <svg class="note-arrow" width="20" height="30" viewBox="0 0 20 30" aria-hidden="true">
    <path d="M10 29 V3 M3 10 L10 3 L17 10" fill="none" stroke="#e0141b" stroke-width="2.5"/>
  </svg>
  <p class="note note--detail">zoomed in front design<br>(letterpress)</p>

  <section class="card card--back-one" aria-label="Card back, option one">
    <ul class="contact">
      <li>0491 270 384</li>
      <li>mvennick@inboxmail.com</li>
      <li>www.martavennick.com</li>
    </ul>
    <div class="band">MARTA VENNICK</div>
  </section>
  <p class="note note--back-one">back design #1</p>

  <section class="card card--back-two" aria-label="Card back, option two">
    <ul class="contact">
      <li>0491 270 384</li>
      <li>mvennick@inboxmail.com</li>
      <li>www.martavennick.com</li>
    </ul>
    <div class="band">MARTA VENNICK</div>
  </section>
  <p class="note note--back-two">back design #2</p>
</body>
</html>
```